Residential Flyer Design Project

This is what im looking for.
Heres what i came up with but it prints blurry. So every thing you see is important i just need the final results to print perfect and with some perfessionals talent applied Im sure we can make this happen.

Target Market(s)

Residential and commercial. Would really like the customer to take advantage of my exclusive offer

Industry/Entity Type

Residential

Requirements
Must have
• Motto. Making Asphalt Great Again
• Phone number. 225-555-0148
• Exclusive offer.
• Service plans. Basic. And the basic elite
• Mascots. Animated worker
• Get to know me page
Nice to have
• Kinda how my flyer looks. Front and back
• Front. Has my service plans and exclusive offer
• Back. Has get to know me.
Should not have
• There's a photo of my competitions flyer next to mine in my diles gotta look better than that

```html
<!DOCTYPE html>
<html lang="en">
<head>
<meta charset="utf-8">
<title>Making Asphalt Great Again – Front and Back Flyer</title>
<link href="https://fonts.googleapis.com/css2?family=Bebas+Neue&family=Roboto+Condensed:ital,wght@0,400;0,700;1,400&display=swap" rel="stylesheet">
<style>
:root{
  --orange:#f47a20;
  --orange-deep:#e2601a;
  --asphalt:#3d3e42;
  --asphalt-dark:#2c2d30;
  --bar:#4a4b4f;
  --paper:#e9eaec;
  --ink:#2b2b2b;
  --white:#ffffff;
  --page:#ececec;
}
*{box-sizing:border-box;margin:0;padding:0}
html,body{width:1200px;height:798px;overflow:hidden;background:var(--page)}
body{position:relative;font-family:"Roboto Condensed",Arial Narrow,sans-serif;color:var(--ink)}
.flyer{position:absolute;top:72px;width:503px;height:646px;background:var(--paper);overflow:hidden;box-shadow:0 3px 10px rgba(0,0,0,.25)}
.flyer--front{left:90px}
.flyer--back{left:610px}
.abs{position:absolute}
.display{font-family:"Bebas Neue",Impact,sans-serif;font-weight:400;letter-spacing:.5px}
.header{left:0;top:0;width:100%;height:72px;background:linear-gradient(90deg,var(--orange),#f58a34 50%,var(--orange));display:flex;align-items:center;justify-content:center}
.header h1{font-family:"Bebas Neue",Impact,sans-serif;font-weight:400;color:var(--white);font-size:47px;line-height:1;padding-top:4px}
.footer{left:0;bottom:0;width:100%;height:43px;background:var(--orange);display:flex;align-items:center;justify-content:center;gap:18px;color:var(--white);font-size:24px;padding-top:2px}
.footer .phone{display:flex;align-items:center;gap:8px}
.icon-phone{width:24px;height:24px}
.brand{display:flex;align-items:center;gap:6px;color:var(--white);font-family:"Roboto Condensed",sans-serif;font-weight:700}
.brand__mark{width:14px;height:14px;background:var(--white)}
.stripe-band{background:linear-gradient(90deg,var(--orange),var(--orange-deep))}
.asphalt{background:radial-gradient(circle at 40% 30%,#4a4b50,var(--asphalt) 60%,var(--asphalt-dark))}
.mascot{background:linear-gradient(180deg,rgba(255,255,255,.22),rgba(255,255,255,.08));border-radius:4px}
.badge{border-radius:50%;background:var(--orange-deep);border:2px solid var(--white);color:var(--white);display:flex;align-items:center;justify-content:center;text-align:center;font-size:9.5px;line-height:1.25;box-shadow:0 1px 4px rgba(0,0,0,.35)}

/* front */
.hero-photo{left:0;top:72px;width:100%;height:188px;background:linear-gradient(160deg,#8aa572 0%,#5b7446 35%,#3b3c3f 70%,#2f3033 100%)}
.hero-brand{right:44px;top:168px;font-size:20px}
.front-stripe{left:0;top:260px;width:100%;height:32px}
.plans{left:0;top:292px;width:100%;height:208px}
.plans__title{left:0;top:10px;width:100%;text-align:center;color:var(--white);font-weight:700;font-size:15.5px;letter-spacing:.3px}
.plans__rule{left:20px;right:20px;top:33px;height:1px;background:rgba(255,255,255,.4)}
.plans__mascot{left:24px;top:40px;width:72px;height:160px}
.plan{top:42px;width:190px;color:var(--white)}
.plan--basic{left:102px;width:186px}
.plan--elite{left:292px;width:198px}
.plan h3{font-family:"Bebas Neue",sans-serif;font-weight:400;color:var(--orange);font-size:16px;display:flex;align-items:center;gap:5px;margin-bottom:3px}
.plan h3 span.chev{font-family:"Roboto Condensed",sans-serif;font-weight:700;font-size:17px}
.plan ul{list-style:none}
.plan li{position:relative;padding-left:11px;font-size:8px;line-height:11px}
.plan li::before{content:"";position:absolute;left:1px;top:2.5px;width:4px;height:6px;border:solid var(--orange);border-width:0 1.5px 1.5px 0;transform:rotate(40deg)}
.offer-bar{left:0;top:500px;width:100%;height:34px;background:var(--bar);display:flex;align-items:center;justify-content:center;font-size:23px;gap:6px;padding-top:2px}
.offer-bar .hl{color:var(--orange)}
.offer-bar .lt{color:var(--white)}
.offer-list{left:18px;top:540px;list-style:none}
.offer-list li{display:flex;align-items:center;gap:6px;font-size:10.5px;height:20px}
.tick-box{width:11px;height:11px}
.front-badge{left:418px;top:532px;width:66px;height:66px}

/* back */
.intro{left:0;top:72px;width:100%;height:176px}
.intro-brand{left:24px;top:150px;font-size:15px}
.intro-ask{left:141px;top:91px;width:220px;color:var(--orange);font-weight:700;font-size:15px;line-height:18.5px;letter-spacing:.3px}
.intro-phone{left:141px;top:151px;display:flex;align-items:center;gap:8px;color:var(--white);font-family:"Roboto Condensed",sans-serif;font-weight:700;font-size:21px}
.intro-call{left:141px;top:180px;color:var(--white);font-weight:700;font-size:15px;letter-spacing:.4px}
.back-stripe{left:78px;top:212px;width:440px;height:36px}
.back-mascot{left:404px;top:62px;width:78px;height:200px;background:linear-gradient(180deg,rgba(255,255,255,.35),rgba(255,255,255,.15))}
.back-badge{left:10px;top:202px;width:68px;height:68px}
.about{left:18px;top:284px;width:328px;font-size:8.9px;line-height:13.4px}
.about h2{font-family:"Roboto Condensed",sans-serif;font-weight:700;color:var(--orange);font-size:15px;margin-bottom:10px;letter-spacing:.3px}
.about p{margin-bottom:13px}
.about .o{color:var(--orange)}
.about .oi{color:var(--orange);font-style:italic}
.about .sign{font-style:italic}
.photo{left:350px;width:132px;border:2px solid var(--white);box-shadow:0 1px 4px rgba(0,0,0,.35)}
.photo--paving{top:286px;height:85px;background:linear-gradient(160deg,#6d6a67,#3a3b3d)}
.photo--beforeafter{top:386px;height:88px;background:linear-gradient(180deg,#647c50,#3b3c3e)}
.photo--driveway{top:490px;height:84px;background:linear-gradient(180deg,#8fa98a,#333436)}
</style>
</head>
<body>

<section class="flyer flyer--front" aria-label="Flyer front">
  <header class="abs header"><h1>Making Asphalt Great Again</h1></header>

  <div class="abs hero-photo" role="img" aria-label="Photo of a freshly sealed parking lot with apartments and trees"></div>
  <div class="abs brand hero-brand"><span class="brand__mark"></span>Mr. Blacktop</div>

  <div class="abs stripe-band front-stripe" role="img" aria-label="Orange and black caution stripe band"></div>

  <div class="abs asphalt plans">
    <h2 class="abs plans__title">RESIDENTAL ASPHALT MAINTENANCE &amp; REPAIR SERVICE PLANS</h2>
    <div class="abs plans__rule"></div>
    <div class="abs mascot plans__mascot" role="img" aria-label="Worker mascot illustration giving a thumbs up"></div>

    <div class="abs plan plan--basic">
      <h3><span class="chev" aria-hidden="true">»</span>BASIC SERVICE</h3>
      <ul>
        <li>Remove all overgrowth from asphalt</li>
        <li>Brush dirt and blow debris away</li>
        <li>Burn and prime oil spots</li>
        <li>Any cracks (¼"x¼") are repaired<br>with putty grade filler</li>
        <li>Using "The flood style application Process"</li>
        <li>Our specialist will brush in an even coat of our special blend of additives and silica sand added to our sealcoat for maximum resistance and durability in the end results.</li>
      </ul>
    </div>

    <div class="abs plan plan--elite">
      <h3><span class="chev" aria-hidden="true">»</span>PREFERRED BASIC ELITE SERVICE</h3>
      <ul>
        <li>A two part in one day application process</li>
        <li>Edge overgrowth from asphalt</li>
        <li>Brush dirt and blow debris away</li>
        <li>Burn and prime oil stains</li>
        <li>Pressure wash all areas of asphalt being sealed</li>
        <li>Any cracks (¼"x¼") are repaired with hot rubbeer commercial grade filler</li>
        <li>Using "The flood style application process"</li>
        <li>Our specialist will brush in an even coat of our special blend of additives and silica sand added to our sealcoat for maximum resistance and durability</li>
      </ul>
    </div>
  </div>

  <div class="abs offer-bar display"><span class="hl">EXCLUSIVE OFFER TO SAVE MONEY!!!</span><span class="lt">TAKE ADVANTAGE</span></div>

  <ul class="abs offer-list">
    <li><svg class="tick-box" viewBox="0 0 12 12" aria-hidden="true"><rect x="1" y="2" width="9" height="9" fill="none" stroke="#f47a20" stroke-width="1.4"/><path d="M3 6l2.5 2.5L11 1.5" fill="none" stroke="#f47a20" stroke-width="1.6"/></svg>Get a friend to use those blacktop guys and get an FREE SERVICE UPGRADE</li>
    <li><svg class="tick-box" viewBox="0 0 12 12" aria-hidden="true"><rect x="1" y="2" width="9" height="9" fill="none" stroke="#f47a20" stroke-width="1.4"/><path d="M3 6l2.5 2.5L11 1.5" fill="none" stroke="#f47a20" stroke-width="1.6"/></svg>Get two friend with equal value or more to your estimate and get a FREE BASIC SERVICE</li>
    <li><svg class="tick-box" viewBox="0 0 12 12" aria-hidden="true"><rect x="1" y="2" width="9" height="9" fill="none" stroke="#f47a20" stroke-width="1.4"/><path d="M3 6l2.5 2.5L11 1.5" fill="none" stroke="#f47a20" stroke-width="1.6"/></svg>Three or more with equal value or more and get a FREE BASIC ELITE SERVICE</li>
  </ul>
  <div class="abs badge front-badge">Call today<br>for your<br>FREE estimate!</div>

  <footer class="abs footer display">
    <span>CALL THOSE BLACKTOP GUYS</span>
    <span class="phone"><svg class="icon-phone" viewBox="0 0 24 24" aria-hidden="true"><circle cx="11" cy="11" r="8.5" fill="none" stroke="#fff" stroke-width="2"/><path d="M17 17l5 5" stroke="#fff" stroke-width="2.4"/><path d="M8 7c0 4 3 7 7 7l-1.5-2.5-2 .5-2-2 .5-2z" fill="#fff"/></svg>(225) 555 0148</span>
  </footer>
</section>

<section class="flyer flyer--back" aria-label="Flyer back">
  <header class="abs header"><h1>Making Asphalt Great Again</h1></header>

  <div class="abs asphalt intro"></div>
  <div class="abs brand intro-brand"><span class="brand__mark"></span>Mr. Blacktop</div>
  <p class="abs intro-ask">DOES YOUR DRIVEWAY NEED ASPHALT MAINTENANCE AND REPAIRS?</p>
  <p class="abs intro-phone"><svg class="icon-phone" viewBox="0 0 24 24" aria-hidden="true"><circle cx="11" cy="11" r="8.5" fill="none" stroke="#fff" stroke-width="2"/><path d="M17 17l5 5" stroke="#fff" stroke-width="2.4"/><path d="M8 7c0 4 3 7 7 7l-1.5-2.5-2 .5-2-2 .5-2z" fill="#fff"/></svg>(225) 555 0148</p>
  <p class="abs intro-call">CALL THOSE BLACKTOP GUYS</p>
  <div class="abs stripe-band back-stripe" role="img" aria-label="Orange and black caution stripe band"></div>
  <div class="abs mascot back-mascot" role="img" aria-label="Worker mascot illustration giving a thumbs up"></div>
  <div class="abs badge back-badge">Call today<br>for your<br>FREE estimate!</div>

  <article class="abs about">
    <h2>GET TO KNOW ME...</h2>
    <p>I want to thank you for the time it takes for you to read this. My name is <span class="o">DARIO</span>. You know me from <span class="o">SUMMIT PAVING</span> and sometime in the past we have done good business together when I maintenance your asphalt (Sealcoat).</p>
    <p>I recently made the desision to live summit and start <span class="o">"Those Blacktop Guys"</span>. It was not an easy choice to leave the security of a weekly paycheck and start a business with the hope theres room for me in this field.<br>My expectation and standards are set at a professional level wheras Summit has recently lost that ambition to put out quality work. That made it easy for me to leave knowing that I way to much pride in my work to settle for any thing less. So today I offer <span class="oi">Better service with better standards</span> asking for you to grow with me and get the results you deserve.</p>
    <p>Take a look at what I have to offer and if it is something you are intersted in call and set up your walk through estimate.</p>
    <p>With the <span class="o">"Making Asphalt Great Again"</span> motto I intend to do just that.</p>
    <p>Again Thank you for your time and hope to hear from you soon.</p>
    <p class="sign">God Bless</p>
  </article>

  <div class="abs photo photo--paving" role="img" aria-label="Photo of a paving roller laying fresh asphalt"></div>
  <div class="abs photo photo--beforeafter" role="img" aria-label="Before and after photos of a sealed driveway"></div>
  <div class="abs photo photo--driveway" role="img" aria-label="Photo of a freshly sealed home driveway"></div>

  <footer class="abs footer display">
    <span>CALL THOSE BLACKTOP GUYS</span>
    <span class="phone"><svg class="icon-phone" viewBox="0 0 24 24" aria-hidden="true"><circle cx="11" cy="11" r="8.5" fill="none" stroke="#fff" stroke-width="2"/><path d="M17 17l5 5" stroke="#fff" stroke-width="2.4"/><path d="M8 7c0 4 3 7 7 7l-1.5-2.5-2 .5-2-2 .5-2z" fill="#fff"/></svg>(225) 555 0148</span>
  </footer>
</section>

</body>
</html>
```